Healthcare technology firm needs business card layout. Logo provided.

We need a business card design for a new healthcare technology company called Kevrimo.com. The logo is already done so that will be used in the design. We assist patients and their families manage their personal health finances. Our initial product is our web site membership that includes educational content on your health benefits, tools, and downloadable forms.

We would like to see designs that use our existing logo or extend the logo in a creative way. Should be very consumer friendly.

```html
<!DOCTYPE html>
<html lang="en">
<head>
<meta charset="utf-8">
<title>Kevrimo business card</title>
<link rel="stylesheet" href="https://fonts.googleapis.com/css2?family=Questrial&display=swap">
<style>
  :root {
    --bg: #e6e9ec;
    --card-white: #ffffff;
    --blue-top: #2a8fd6;
    --blue-bottom: #0b4fa8;
    --brand-blue: #1a5fb4;
    --green: #3bb54a;
    --ink: #2b2b2b;
    --shadow: rgba(20, 40, 60, 0.22);
  }
  * { box-sizing: border-box; margin: 0; padding: 0; }
  html, body { width: 1200px; height: 960px; overflow: hidden; }
  body {
    background: var(--bg);
    font-family: "Questrial", "Century Gothic", sans-serif;
    color: var(--ink);
  }
  .canvas {
    width: 1200px; height: 960px;
    display: flex; flex-direction: column;
    align-items: center; justify-content: center;
    gap: 80px;
  }
  .card {
    width: 560px; height: 320px;
    position: relative;
    box-shadow: 0 10px 30px var(--shadow);
  }
  /* Front */
  .card--front {
    background: linear-gradient(180deg, var(--blue-top) 0%, var(--blue-bottom) 100%);
  }
  .front-brand {
    position: absolute; right: 36px; bottom: 88px;
    display: flex; align-items: center; gap: 12px;
  }
  .front-brand__name {
    color: var(--card-white);
    font-size: 46px; letter-spacing: 1px; line-height: 1;
  }
  .front-brand__dot {
    width: 16px; height: 16px; border-radius: 50%;
    background: var(--green);
  }
  /* Back */
  .card--back {
    background: var(--card-white);
    padding: 30px 40px 30px;
    display: flex; flex-direction: column;
  }
  .back-brand {
    text-align: center;
    color: var(--brand-blue);
    font-size: 46px; font-weight: 400; letter-spacing: 2px; line-height: 1;
  }
  .person {
    text-align: center; margin-top: 22px;
    font-size: 20px; line-height: 1.2;
  }
  .details {
    display: flex; justify-content: space-between;
    margin-top: 24px; font-size: 16px; line-height: 1.35;
  }
  .detail-row { display: flex; align-items: flex-start; gap: 12px; }
  .ring {
    flex: none; width: 14px; height: 14px; margin-top: 3px;
    border-radius: 50%;
    border: 4px solid var(--green);
    background: var(--card-white);
    box-shadow: 0 0 0 1px var(--green);
  }
  .contact-list { display: flex; flex-direction: column; gap: 2px; }
  .locations { margin-right: 4px; }
  .tagline {
    text-align: center; margin-top: auto;
    font-size: 17px; letter-spacing: 0.3px;
  }
</style>
</head>
<body>
  <main class="canvas">
    <section class="card card--front" aria-label="Card front">
      <div class="front-brand">
        <span class="front-brand__name">KEVRIMO</span>
        <span class="front-brand__dot"></span>
      </div>
    </section>

    <section class="card card--back" aria-label="Card back">
      <h1 class="back-brand">KEVRIMO</h1>
      <div class="person">
        <p class="person__name">Dana R. Whitfield</p>
        <p class="person__title">CEO</p>
      </div>
      <div class="details">
        <div class="contact-list">
          <div class="detail-row"><span class="ring"></span><span>M: 555-014-2760</span></div>
          <div class="detail-row"><span class="ring"></span><span>www.kevrimo.com</span></div>
        </div>
        <div class="detail-row locations">
          <span class="ring"></span>
          <span>Lakeview<br>Harbor Pines<br>Redmesa, Northgate</span>
        </div>
      </div>
      <p class="tagline">Making your care costs simpler</p>
    </section>
  </main>
</body>
</html>
```